Letterhead design for Dental Practice - Ashby Lane Dental Care

Letterhead for Private Dental Practice. To be used for all official correspondance and for printing treatment details on to be given to patients.

Target Market(s)

Private dental patients

Industry/Entity Type

Dental Clinic

Font styles to use
Other font styles liked:
• nexa-light

Colors
33a6d7
1c66ac
85abd2

Requirements
Must have
• info in the footer and header needs to be 3.5cm from upper/lower boader of paper, see photo in uploaded files
• info details:
• tel. 0115 947 3051
• email info@ashbylanedc.co.uk
• ashbylanedentalcare.co.uk
• 17b Ashby Lane West Bridgford Nottingham NG2 7QT
• nexa-light font as in uploaded logo files
Should not have
• No funny tooth pictures

```html
<!DOCTYPE html>
<html lang="en">
<head>
<meta charset="utf-8">
<title>Ashby Lane Dental Care – Letterhead</title>
<link rel="stylesheet" href="https://fonts.googleapis.com/css2?family=Roboto:wght@400&display=swap">
<style>
  :root {
    --brand-blue: #1a9fdc;
    --ink: #4a4a4a;
    --paper: #ffffff;
    --backdrop: #e9e9e9;
  }
  * { margin: 0; padding: 0; box-sizing: border-box; }
  html, body {
    width: 1200px;
    height: 1120px;
    overflow: hidden;
    background: var(--backdrop);
  }
  .letterhead {
    position: absolute;
    left: 199px;
    top: 30px;
    width: 802px;
    height: 1059px;
    background: var(--paper);
    box-shadow: 0 2px 10px rgba(0,0,0,0.12);
  }
  .brand {
    position: absolute;
    left: 71px;
    top: 82px;
    display: flex;
    align-items: center;
    font-family: "Roboto", sans-serif;
    font-weight: 400;
    font-size: 16px;
    line-height: 1;
    color: var(--brand-blue);
    white-space: nowrap;
  }
  .brand-mark {
    width: 22px;
    height: 22px;
    margin-right: 8px;
    border-radius: 50%;
    background: var(--brand-blue);
    flex: none;
  }
  .footer-band {
    position: absolute;
    left: 0;
    top: 995px;
    width: 56px;
    height: 36px;
    background: var(--brand-blue);
  }
  .footer-info {
    position: absolute;
    left: 71px;
    top: 995px;
    font-family: "Roboto", sans-serif;
    font-weight: 400;
    font-size: 11.5px;
    line-height: 16px;
    color: var(--ink);
  }
  .contact-line {
    display: flex;
    align-items: center;
    white-space: nowrap;
  }
  .contact-line svg {
    width: 10px;
    height: 10px;
    margin-right: 5px;
    fill: none;
    stroke: var(--brand-blue);
    stroke-width: 1.6;
  }
  .divider {
    margin: 0 8px;
  }
</style>
</head>
<body>
  <main class="letterhead">
    <header class="brand">
      <span class="brand-mark"></span>
      <span class="brand-name">Ashby Lane Dental Care</span>
    </header>

    <div class="footer-band"></div>
    <footer class="footer-info">
      <p class="address">17b Ashby Lane, West Bridgford, Nottingham NG2 7QT</p>
      <p class="contact-line">
        <svg viewBox="0 0 10 10" aria-hidden="true"><path d="M7.5 1.5 C4 1.5 2 4 2 6.5 L2.5 8.5"/></svg>
        <span>0115 947 3051</span>
        <span class="divider">|</span>
        <svg viewBox="0 0 10 10" aria-hidden="true"><rect x="1" y="2.5" width="8" height="5.5"/><path d="M1 2.5 L5 5.5 L9 2.5"/></svg>
        <span>info@ashbylanedc.co.uk</span>
        <span class="divider">|</span>
        <svg viewBox="0 0 10 10" aria-hidden="true"><circle cx="5" cy="5" r="4"/><path d="M1 5 H9 M5 1 C3 3.5 3 6.5 5 9 M5 1 C7 3.5 7 6.5 5 9"/></svg>
        <span>ashbylanedentalcare.co.uk</span>
      </p>
    </footer>
  </main>
</body>
</html>
```